Kestra Rowe - Contact/Landing Page

I need a landing page which will essentially be the page that customers will go to from the 'website' link on TLX listing. It will provide a short overview of services which need to be selectable. a little further down can capture some contact details followed by a large Submit Now button etc...

I have some icon/logo's that can be utilised at the bottom of the page as industry type references.

Target Market(s)

End of Lease Cleaning Services

Industry/Entity Type

Cleaning Service

Colors

Designer to choose colors to be used in the design.

Requirements
Must have
• As per description
Should not have
• Colours to match my website kestrarowe.com.au

```html
<!DOCTYPE html>
<html lang="en">
<head>
<meta charset="utf-8">
<title>Kestra Rowe – End of Lease Cleaning &amp; Licensed Pest Control</title>
<link rel="stylesheet" href="https://fonts.googleapis.com/css2?family=Roboto:wght@400;500;700&family=Sarabun:wght@400;500&family=Crimson+Text:wght@400;600&display=swap">
<style>
:root{
  --blue:#2f7dc8;
  --blue-deep:#1d5fae;
  --blue-light:#5fb3e6;
  --form-blue:#3a7bc8;
  --ink:#1b1b1b;
  --text:#333;
  --white:#fff;
  --footer:#1a1a1a;
  --link:#2b79c6;
}
*{margin:0;padding:0;box-sizing:border-box}
html,body{width:1200px;height:2647px;overflow:hidden;background:var(--white)}
body{position:relative;font-family:"Sarabun",sans-serif;color:var(--text)}
.abs{position:absolute}

/* hero */
.hero{left:0;top:0;width:1200px;height:650px;overflow:hidden;
  background:linear-gradient(120deg,#3f86cf 0%,#5aa6e0 45%,#3d8fd6 70%,#62b5e8 100%)}
.hero-curve{left:0;top:560px;width:1200px;height:90px}
.top-contact{left:100px;top:16px;display:flex;align-items:center;gap:10px;color:var(--white);font-family:"Roboto",sans-serif}
.top-contact .line1{font-size:15px;font-weight:500}
.top-contact .line2{font-size:16px;font-weight:700;margin-top:2px}
.menu-btn{left:1072px;top:18px}
.brand{left:0;top:250px;width:1200px;text-align:center;font-family:"Roboto",sans-serif;font-weight:700;font-size:92px;line-height:1;color:var(--white);letter-spacing:2px}
.tagline{left:0;top:482px;width:1200px;text-align:center;font-family:"Crimson Text",serif;font-size:38px;color:var(--white)}
.tagline span{margin:0 18px}

/* services */
.section-title{left:0;width:1200px;text-align:center;font-family:"Roboto",sans-serif;font-weight:700;font-size:36px;color:var(--ink)}
.card{width:316px;height:424px;top:744px;background:var(--white);box-shadow:0 1px 6px rgba(0,0,0,.1)}
.card-photo{position:absolute;left:0;top:0;width:316px;height:224px}
.card-arc{position:absolute;left:0;top:196px;width:316px;height:40px}
.card-icon{position:absolute;left:124px;top:160px;width:68px;height:68px;border-radius:50%;background:var(--blue);border:3px solid var(--white);display:flex;align-items:center;justify-content:center}
.card h3{position:absolute;top:240px;left:0;width:100%;text-align:center;font-family:"Crimson Text",serif;font-weight:400;font-size:35px;color:var(--ink)}
.card p{position:absolute;top:288px;left:24px;width:268px;text-align:center;font-size:18px;line-height:28px;color:var(--text)}
.select{position:absolute;top:384px;left:0;width:100%;text-align:center;font-family:"Roboto",sans-serif;font-size:16px;font-weight:500;color:var(--link);display:flex;justify-content:center;align-items:center;gap:10px}
.select i{display:inline-block;width:15px;height:15px;border:2px solid var(--link)}

/* quote */
.quote{left:0;top:1330px;width:1200px;height:592px;overflow:hidden}
.quote-photo{position:absolute;left:0;top:0;width:1200px;height:592px;background:linear-gradient(90deg,#c9cfd7 0%,#e6e9ee 50%,#eef0f3 100%)}
.quote-bg{position:absolute;left:0;top:0}
.quote-box{left:552px;top:1404px;width:435px;height:445px;background:var(--form-blue);padding:26px 40px}
.quote-box h2{font-family:"Roboto",sans-serif;font-weight:700;font-size:38px;color:var(--white);margin-bottom:14px}
.field{width:350px;height:46px;border:2px solid var(--white);color:var(--white);font-size:17px;padding:0 19px;display:flex;align-items:center;margin-bottom:9px}
.form-foot{display:flex;align-items:center;margin-top:6px}
.submit{width:134px;height:46px;border:2px solid var(--white);color:var(--white);font-family:"Roboto",sans-serif;font-weight:700;font-size:16px;display:flex;align-items:center;justify-content:center}
.mail{margin-left:12px;display:flex;align-items:center;gap:6px;color:var(--white);font-size:15px;line-height:22px}

/* clients */
.clients{left:92px;top:2076px;width:1010px;display:flex;justify-content:space-between;align-items:center}
.badge{height:60px;border-radius:4px}

/* footer */
.footer{left:0;top:2242px;width:1200px;height:405px;background:var(--footer);color:var(--white)}
.f-brand{left:100px;top:92px;width:150px;text-align:center;font-family:"Roboto",sans-serif;font-weight:700;font-size:40px;line-height:44px;color:var(--blue-light)}
.f-licence{left:100px;top:282px;font-family:"Roboto",sans-serif;font-size:14px;font-weight:500}
.f-col h4{font-family:"Roboto",sans-serif;font-weight:700;font-size:19px;padding-bottom:6px;position:relative}
.f-col h4::after{content:"";position:absolute;left:0;bottom:0;width:40px;height:2px;background:var(--blue)}
.f-col ul{list-style:none;margin-top:14px}
.f-col li{font-size:15px;line-height:29px}
.contact-row{display:flex;align-items:flex-start;gap:10px;font-size:15px;line-height:24px}
.c-ico{width:34px;height:34px;border-radius:50%;background:var(--white);flex:none;display:flex;align-items:center;justify-content:center}
.divider{left:100px;top:343px;width:1000px;height:1px;background:#444}
.copy{left:0;top:368px;width:1200px;text-align:center;font-size:15px}
</style>
</head>
<body>

<!-- HERO -->
<header class="hero abs" role="img" aria-label="Blurred photo of a gloved hand holding cleaning spray bottles">
  <div class="top-contact abs" style="left:100px;top:16px">
    <svg width="40" height="40" viewBox="0 0 40 40" fill="none" stroke="#fff" stroke-width="2"><circle cx="18" cy="22" r="12"/><path d="M12 22a6 6 0 0 1 12 0"/><rect x="26" y="4" width="12" height="9" rx="1"/></svg>
    <div><div class="line1">HOUSE CLEANING AND PEST CONTROL</div><div class="line2">CALL / SMS 0428 715 936</div></div>
  </div>
  <svg class="menu-btn abs" width="28" height="24" viewBox="0 0 28 24"><rect y="2" width="28" height="3" fill="#fff"/><rect y="11" width="28" height="3" fill="#fff"/><rect y="20" width="28" height="3" fill="#fff"/></svg>
  <div class="brand abs">KESTRA<br>ROWE</div>
  <div class="tagline abs">End of Lease Cleaning<span>|</span>Licensed Pest Control</div>
  <svg class="hero-curve abs" viewBox="0 0 1200 90" preserveAspectRatio="none">
    <path d="M0 90 Q600 -40 1200 90 Z" fill="#fff"/>
    <path d="M0 90 Q600 -40 1200 90" fill="none" stroke="#111" stroke-width="5"/>
  </svg>
</header>

<!-- WHAT WE DO -->
<h2 class="section-title abs" style="top:672px">WHAT WE DO</h2>

<article class="card abs" style="left:100px">
  <div class="card-photo" role="img" aria-label="Bucket of colourful cleaning products and gloves" style="background:linear-gradient(135deg,#f1b431,#3d8fd0 55%,#9fd3c0)"></div>
  <svg class="card-arc" viewBox="0 0 316 40" preserveAspectRatio="none"><path d="M0 40 Q158 -10 316 40 Z" fill="#fff"/><path d="M0 30 Q158 -10 316 30" fill="none" stroke="#2f7dc8" stroke-width="3"/></svg>
  <div class="card-icon"><svg width="32" height="32" viewBox="0 0 32 32" fill="none" stroke="#fff" stroke-width="2"><path d="M8 28V14h10v14zM12 14V8h4v6M18 18h6l2 10"/></svg></div>
  <h3>Cleaning</h3>
  <p>All interior cleaning carried out to property management requirements</p>
  <div class="select">SELECT <i></i></div>
</article>

<article class="card abs" style="left:442px">
  <div class="card-photo" role="img" aria-label="Vacuuming a carpet in a bright living room" style="background:linear-gradient(135deg,#c8c4bd,#e9e6e1 50%,#a9a29a)"></div>
  <svg class="card-arc" viewBox="0 0 316 40" preserveAspectRatio="none"><path d="M0 40 Q158 -10 316 40 Z" fill="#fff"/><path d="M0 30 Q158 -10 316 30" fill="none" stroke="#2f7dc8" stroke-width="3"/></svg>
  <div class="card-icon"><svg width="32" height="32" viewBox="0 0 32 32" fill="none" stroke="#fff" stroke-width="2"><rect x="6" y="6" width="20" height="20"/><path d="M10 12h12M10 18h12"/></svg></div>
  <h3>Carpet Cleaning</h3>
  <p>Carpet stacam cleaning to Australian Standard As 3733:1995</p>
  <div class="select">SELECT <i></i></div>
</article>

<article class="card abs" style="left:784px">
  <div class="card-photo" role="img" aria-label="Pest spray applied along a timber floor" style="background:linear-gradient(135deg,#8f8a86,#d9d4cf 45%,#8a5a2e)"></div>
  <svg class="card-arc" viewBox="0 0 316 40" preserveAspectRatio="none"><path d="M0 40 Q158 -10 316 40 Z" fill="#fff"/><path d="M0 30 Q158 -10 316 30" fill="none" stroke="#2f7dc8" stroke-width="3"/></svg>
  <div class="card-icon"><svg width="32" height="32" viewBox="0 0 32 32" fill="none" stroke="#fff" stroke-width="2"><circle cx="12" cy="8" r="3"/><path d="M12 11v10l-4 7M12 21l4 7M14 14l8 4"/></svg></div>
  <h3>Pest Control</h3>
  <p>Mandatory requirement for pets on premises</p>
  <div class="select">SELECT <i></i></div>
</article>

<!-- REQUEST A QUOTE -->
<section class="quote abs">
  <div class="quote-photo" role="img" aria-label="Pest technician in overalls reviewing a clipboard with a customer in a kitchen"></div>
  <svg class="quote-bg" width="1200" height="592" viewBox="0 0 1200 592">
    <defs><linearGradient id="qg" x1="0" y1="0" x2="1" y2="1"><stop offset="0" stop-color="#3b7fc9"/><stop offset="1" stop-color="#5cb4e8"/></linearGradient></defs>
    <polygon points="918,0 1200,0 1200,592 680,592" fill="url(#qg)"/>
  </svg>
</section>
<form class="quote-box abs">
  <h2>REQUEST A QUOTE</h2>
  <div class="field">First Name*</div>
  <div class="field">sur Name*</div>
  <div class="field">Email*</div>
  <div class="field">Phone*</div>
  <div class="field">Suburb*</div>
  <div class="form-foot">
    <div class="submit">SUBMIT</div>
    <div class="mail">
      <svg width="42" height="30" viewBox="0 0 42 30" fill="none" stroke="#fff" stroke-width="2.5"><rect x="2" y="2" width="38" height="26"/><path d="M2 2l19 15L40 2"/></svg>
      <div>Email<br>info@kestrarowe.com.au</div>
    </div>
  </div>
</form>

<!-- CLIENTS -->
<h2 class="section-title abs" style="top:2008px">OUR CLIENTS</h2>
<div class="clients abs">
  <div class="badge" style="width:154px;background:#1d1d1d"></div>
  <div class="badge" style="width:184px;height:50px;background:#c9d3e6"></div>
  <div class="badge" style="width:106px;height:64px;background:#d3dcec"></div>
  <div class="badge" style="width:190px;height:56px;background:#8ab84a"></div>
  <div class="badge" style="width:104px;height:62px;background:#cfdbe9"></div>
</div>

<!-- FOOTER -->
<footer class="footer abs">
  <div class="f-brand abs">KESTRA<br>ROWE</div>
  <div class="f-licence abs">PETS LICENCE: 5170364</div>

  <div class="f-col abs" style="left:375px;top:88px">
    <h4>MENU</h4>
    <ul><li>Home</li><li>About Us</li><li>Services</li><li>Clients</li><li>Contact Us</li></ul>
  </div>

  <div class="f-col abs" style="left:617px;top:88px;width:260px">
    <h4>CONTACT US</h4>
    <div class="contact-row" style="margin-top:18px">
      <span class="c-ico"><svg width="14" height="18" viewBox="0 0 14 18"><path d="M7 0a7 7 0 0 1 7 7c0 5-7 11-7 11S0 12 0 7a7 7 0 0 1 7-7z" fill="#2f7dc8"/><circle cx="7" cy="7" r="2.5" fill="#fff"/></svg></span>
      <span>24 Marlow Ct, Ferndale NSW<br>2768, Australia</span>
    </div>
    <div class="contact-row" style="margin-top:16px;align-items:center">
      <span class="c-ico"><svg width="16" height="16" viewBox="0 0 16 16"><path d="M3 1l3 3-2 2c1 2 3 4 5 5l2-2 3 3-2 3C6 14 2 10 1 3z" fill="#2f7dc8"/></svg></span>
      <span>0428 715 936</span>
    </div>
    <div class="contact-row" style="margin-top:22px;align-items:center">
      <span class="c-ico"><svg width="18" height="13" viewBox="0 0 18 13" fill="none" stroke="#2f7dc8" stroke-width="1.8"><rect x="1" y="1" width="16" height="11"/><path d="M1 1l8 6 8-6"/></svg></span>
      <span>info@kestrarowe.com.au</span>
    </div>
  </div>

  <div class="f-col abs" style="left:994px;top:88px">
    <h4>SERVICES</h4>
    <ul style="margin-top:18px"><li>Cleaning</li><li>Carpet Cleaning</li><li>pest Control</li></ul>
    <div style="width:34px;height:34px;border-radius:50%;background:#fff;margin-top:12px;margin-left:-3px"></div>
  </div>

  <div class="divider abs"></div>
  <div class="copy abs">© 2021 KESTRA ROWE. All Rights Reserved.</div>
</footer>

</body>
</html>
```